Kes-Trindle web design

We need a homepage web design with final files to be provided in PSD for a company based in Brisbane called 'Kes-Trindle'. They provide innovative and reliable contract packaging solutions for local and national outsourcing buisnesses.

They have an existing website www.kes-trindle.com.au that is in dire need of an update to look more professional and sleek.

Target Market(s)

Engineers, Architects

Industry/Entity Type

Construction

Number of Pages Required

1 page

Requirements
Must have
• Main Navigation
• o Home
• o About Us
• o Spacers
• - Standard Cage Wheel Spacer
• - Heavy Duty Cage Wheel Spacer
• - Pile Cage Foot
• - PreCast Piles
• o Packaging
• o Injection Moulding
• o News
• o Contact Us
• - Client wants an updated more professional look and feel that aligns with their branding.
• - Client likes the use of displaying Products on every page eg www.gravelnook.com that has an image of the product and its name obviously looking better than this.
• The following elements are to be included in the Homepage design concept:
• - Room for a Flash banner of rotating images
• - Horizontal navigation (can you show how drop down will appear as well)
• - Logo is attached
• - Phone number needs to appear prominently on every page 07 3190 4856
• - Use Arial font throughout concept incl logo
• - Intro text on page somewhere
• - Products need to be listed on page somewhere there are 7 products (image and name with click through)
• - 2 containers/icons to highlight areas on site Latest News and Contact Us
• - Images – have attached a few that can be used in concepts and also below are some pixmarrow images that could be used in banner:
• http://www.pixmarrowfoto.com/stock-photo-4820316-several-paint-buckets.php
• http://www.pixmarrowfoto.com/stock-photo-3157840-cans-of-paint.php
• http://www.pixmarrowfoto.com/stock-photo-2748391-reinforcing-steel.php
• http://www.pixmarrowfoto.com/stock-photo-8063412-huge-bridge-pier.php
• http://www.pixmarrowfoto.com/stock-photo-1592874-highway-bridge.php
• http://www.pixmarrowfoto.com/stock-photo-4306159-bridge.php
• http://www.pixmarrowfoto.com/stock-photo-2684037-bridge-to-nowhere-yet.php

```html
<!DOCTYPE html>
<html lang="en">
<head>
<meta charset="utf-8">
<title>Kes-Trindle – Home</title>
<link href="https://fonts.googleapis.com/css2?family=Arimo:wght@400;700&display=swap" rel="stylesheet">
<style>
:root{
  --page-bg:#4a1d20;
  --brand-red:#8e2024;
  --brand-red-dark:#6e1518;
  --tile-red:#a9484b;
  --lavender:#7b78b8;
  --panel-grey:#f2f2f2;
  --text:#222;
  --news-red:#8e2024;
  --white:#fff;
}
*{box-sizing:border-box;margin:0;padding:0}
html,body{width:933px;height:1200px;overflow:hidden}
body{background:var(--page-bg);font-family:"Arimo",Arial,sans-serif;color:var(--text);position:relative}
.site{position:absolute;left:44px;top:0;width:845px;height:1144px}
.header{position:absolute;left:0;top:0;width:845px;height:107px;background:linear-gradient(#fafafa,#d9d9d9)}
.brand{position:absolute;left:48px;top:34px;display:flex;align-items:center;gap:10px;font-size:20px;font-weight:700;color:var(--brand-red)}
.brand-dot{width:22px;height:22px;border-radius:50%;background:var(--brand-red)}
.phone{position:absolute;right:28px;top:20px;display:flex;align-items:center;gap:8px;color:var(--brand-red);font-size:17px;font-weight:700}
.nav-strip{position:absolute;left:0;top:133px;width:845px;height:26px;background:linear-gradient(#cfcfcf,#b5b5b5);border-radius:0 0 16px 16px}
.nav{position:absolute;left:0;top:107px;width:845px;height:26px;background:var(--brand-red);display:flex;list-style:none}
.nav li{height:26px;line-height:26px;color:var(--white);font-size:13.5px;text-align:center}
.nav li.active{background:var(--brand-red-dark)}
.dropdown{position:absolute;left:282px;top:135px;width:200px;list-style:none;background:rgba(110,21,24,.92);z-index:3}
.dropdown li{height:29px;line-height:29px;padding-left:12px;color:var(--white);font-size:13px;border-bottom:1px solid #8f3d49}
.dropdown li:last-child{border-bottom:none}
.main{position:absolute;left:0;top:193px;width:845px;height:880px;background:#fbfbfb}
.banner{position:absolute;left:19px;top:19px;width:580px;height:213px;background:linear-gradient(#7fb1e0 0%,#bcd3e6 45%,#9a9387 70%,#b9ad9a 100%)}
.banner-caption{position:absolute;left:0;bottom:0;width:100%;height:70px;background:rgba(135,128,180,.8);display:flex;align-items:center;padding-left:26px;gap:14px}
.banner-caption h2{font-size:27px;font-weight:400;color:var(--white);letter-spacing:1.5px}
.banner-caption a{color:var(--white);font-size:12px;text-decoration:underline}
.welcome{position:absolute;left:19px;top:243px;width:580px;height:173px;background:linear-gradient(#e2e1ec,#f3f3fa);padding:20px 32px}
.welcome h1{font-size:24px;font-weight:400;color:var(--lavender);letter-spacing:1px;margin-bottom:18px}
.welcome p{font-size:15px;line-height:19px;margin-bottom:12px}
.products{position:absolute;left:19px;top:430px;width:580px;height:428px;background:var(--panel-grey)}
.section-title{display:flex;align-items:center;gap:10px;font-size:17px;color:var(--news-red)}
.products .section-title{position:absolute;left:16px;top:10px;width:547px;padding-bottom:7px;border-bottom:1px solid #888}
.divider{position:absolute;left:332px;top:57px;width:1px;height:320px;background:#888}
.tile{position:absolute;width:229px;height:79px;background:var(--tile-red);display:flex;align-items:center;justify-content:space-between;padding:0 8px 0 10px}
.tile a{color:var(--white);font-size:15px;text-decoration:underline}
.tile-img{width:62px;height:56px;background:linear-gradient(#f0f0f0,#6a6a6a)}
.sidebar{position:absolute;left:611px;top:19px;width:214px}
.newsletter{position:absolute;left:0;top:0;width:214px;height:147px;background:var(--brand-red);padding:9px 12px;color:var(--white)}
.newsletter h3{font-size:17px;font-weight:700;letter-spacing:.5px;padding-bottom:8px;border-bottom:1px solid #b96066}
.nl-row{display:flex;align-items:center;gap:8px;margin-top:16px;font-size:11px;padding-left:9px}
.nl-input{width:128px;height:14px;background:var(--white)}
.nl-actions{display:flex;gap:6px;margin-top:24px;padding-left:30px}
.nl-select{width:94px;height:17px;border-radius:5px;background:linear-gradient(#fff,#cbd6e6);color:#222;font-size:10px;padding-left:6px;line-height:17px}
.nl-submit{width:52px;height:17px;border-radius:8px;background:linear-gradient(#fff,#ddd);color:#222;font-size:10px;text-align:center;line-height:17px}
.contact-btn{position:absolute;left:20px;top:181px;width:178px;height:44px;border:1px solid var(--brand-red);border-radius:6px;background:linear-gradient(#fff,#d2d2d2);display:flex;align-items:center;justify-content:center;gap:12px;color:var(--brand-red);font-size:16px;font-weight:700;letter-spacing:1px}
.news{position:absolute;left:0;top:264px;width:214px;height:471px;background:var(--panel-grey);padding:12px 18px}
.news .section-title{padding-bottom:4px;border-bottom:1px solid #888;justify-content:space-between}
.news-item{margin-top:22px;font-size:12px;line-height:14px}
.news-item h4{font-weight:400;color:var(--news-red);margin-bottom:16px}
.news-item+.news-item{margin-top:52px}
.footer{position:absolute;left:0;top:1073px;width:845px;height:71px;background:var(--brand-red);border-radius:0 0 18px 18px;color:var(--white);text-align:center;font-size:10.5px;padding-top:18px}
.footer .current{color:#3a0c0e}
.footer p+p{margin-top:20px}
</style>
</head>
<body>
<div class="site">
  <header class="header">
    <div class="brand"><span class="brand-dot"></span>Kes-Trindle</div>
    <div class="phone">
      <svg width="12" height="24" viewBox="0 0 12 24"><path d="M9 1 C3 3 1 8 2 13 C3 18 6 22 10 23 L11 19 C8 18 6 15 6 12 C6 9 7 6 10 5 Z" fill="#8e2024"/></svg>
      07 3190 4856
    </div>
  </header>
  <div class="nav-strip"></div>
  <ul class="nav">
    <li style="width:49px"></li>
    <li class="active" style="width:95px">Home</li>
    <li style="width:89px">About Us</li>
    <li class="active" style="width:96px">Spacers</li>
    <li style="width:105px">Packaging</li>
    <li style="width:152px">Injection Moulding</li>
    <li style="width:78px">News</li>
    <li style="width:106px">Contact Us</li>
  </ul>
  <ul class="dropdown">
    <li>Standard Cage Wheel Spacer</li>
    <li>Heavy Duty Cage Wheel Spacer</li>
    <li>Pile Cage Foot</li>
    <li>PreCast Piles</li>
  </ul>

  <main class="main">
    <section class="banner" role="img" aria-label="Banner photo of a bridge under construction with cranes">
      <div class="banner-caption"><h2>PLANT UPGRADE -</h2><a href="#">more info</a></div>
    </section>

    <section class="welcome">
      <h1>WELCOME TO KTv3!</h1>
      <p>Kes-Trindle Brisbane, providing innovative and reliable contract packaging solutions for local and national outsourcing buisnesses.</p>
      <p>Kes-Trindle Brisbane, providing innovative and reliable contract packaging solutions for local and national outsourcing buisnesses.</p>
    </section>

    <section class="products">
      <h3 class="section-title">
        <svg width="22" height="18" viewBox="0 0 22 18"><rect x="6" y="0" width="16" height="13" fill="#8a88a8"/><rect x="0" y="5" width="13" height="13" fill="#b2b0c8"/></svg>
        Products
      </h3>
      <div class="divider"></div>
      <div class="tile" style="left:32px;top:58px"><a href="#">Pile Wheel varieties</a><div class="tile-img" role="img" aria-label="Product photo of a wheel spacer"></div></div>
      <div class="tile" style="left:32px;top:144px"><a href="#">Pile Wheel varieties</a><div class="tile-img" role="img" aria-label="Product photo of two bronze spacers" style="background:linear-gradient(#a9484b,#8c7640)"></div></div>
      <div class="tile" style="left:32px;top:230px"><a href="#">Pile Wheel varieties</a><div class="tile-img" role="img" aria-label="Product photo of coloured plastic caps" style="background:linear-gradient(#e0e0e0,#2f6e7a)"></div></div>
      <div class="tile" style="left:32px;top:316px"><a href="#">Pile Wheel varieties</a><div class="tile-img" role="img" aria-label="Product photo of grey moulded parts" style="background:linear-gradient(#f2f2f2,#555)"></div></div>
      <div class="tile" style="left:316px;top:58px"><a href="#">Pile Wheel varieties</a><div class="tile-img" role="img" aria-label="Product photo of black cage feet" style="background:linear-gradient(#f4f4f4,#222)"></div></div>
      <div class="tile" style="left:316px;top:144px"><a href="#">Pile Wheel varieties</a><div class="tile-img" role="img" aria-label="Product photo of a black heavy duty wheel" style="background:linear-gradient(#f4f4f4,#1a1a1a)"></div></div>
      <div class="tile" style="left:316px;top:230px"><a href="#">Pile Wheel varieties</a><div class="tile-img" role="img" aria-label="Product photo of a black hex cap" style="background:linear-gradient(#f4f4f4,#2a2a2a)"></div></div>
    </section>

    <aside class="sidebar">
      <form class="newsletter">
        <h3>Sign up for newsletter</h3>
        <div class="nl-row"><span>email :</span><span class="nl-input"></span></div>
        <div class="nl-actions"><span class="nl-select">Subscribe ▾</span><span class="nl-submit">submit</span></div>
      </form>
      <a class="contact-btn" href="#">CONTACT US
        <svg width="24" height="16" viewBox="0 0 24 16"><rect x=".5" y=".5" width="23" height="15" fill="#fff" stroke="#999"/><path d="M1 1 L12 9 L23 1" fill="none" stroke="#999"/></svg>
      </a>
      <section class="news">
        <h3 class="section-title">
          <span style="display:flex;align-items:center;gap:10px">
            <svg width="22" height="18" viewBox="0 0 22 18"><rect x="6" y="0" width="16" height="13" fill="#8a88a8"/><rect x="0" y="5" width="13" height="13" fill="#b2b0c8"/></svg>
            Latest News
          </span>
          <svg width="16" height="16" viewBox="0 0 16 16"><rect width="16" height="16" rx="3" fill="#e8792a"/><circle cx="4.5" cy="11.5" r="1.6" fill="#fff"/><path d="M3 7 A6 6 0 0 1 9 13 M3 3.5 A9.5 9.5 0 0 1 12.5 13" fill="none" stroke="#fff" stroke-width="1.6"/></svg>
        </h3>
        <article class="news-item">
          <h4>1/08/07 || Product News<br>&nbsp;-Spacers Range extended</h4>
          <p>The tooling has now been completed and the Heavy Duty range of easy to fit spacers are now available and in stock...</p>
        </article>
        <article class="news-item">
          <h4>23/08/06 || Product News<br>&nbsp;-New Innovative Spacer</h4>
          <p>We have developed a heavy duty 50mm cover spacer that can be attached to the cage with an ‘easy tap’ click on fitting...</p>
        </article>
        <article class="news-item">
          <h4>24/07/04 || Product News<br>&nbsp;-PRODUCT IMPROVEMENT</h4>
          <p>The 75mm cover ‘Hinged Wheel’ spacer has been a very popular product in the concrete pile construction business ...</p>
        </article>
      </section>
    </aside>
  </main>

  <footer class="footer">
    <p>| <span class="current">Home</span> | About Us | Spacer | Cabins | Packaging | Injection Moulding | News | Contact Us</p>
    <p>Copyright @ Kes-Trindle 2009</p>
  </footer>
</div>
</body>
</html>
```